Quorvex business card design

create modern and tech looking business card that is clean but effectively communciates that we are a cloud communications company.
Should have at minimum:
Employee Name
Postion
Phone Number
Email
website
create modern and tech looking business card that is clean but effectively communciates that we are a cloud communications company. We have two logo color schemes (attached) so would like to see designs both ways
Should have at minimum:
Employee Name
Postion
Phone Number
Email
website

```html
<!DOCTYPE html>
<html lang="en">
<head>
<meta charset="utf-8">
<title>Quorvex business card</title>
<link href="https://fonts.googleapis.com/css2?family=Exo+2:wght@400;500;600;700&display=swap" rel="stylesheet">
<style>
  :root {
    --bg: #3b3b3d;
    --purple-deep: #35115c;
    --purple: #56208a;
    --cyan: #3bb4dc;
    --ink: #2f2f33;
    --ink-soft: #555560;
    --paper: #ffffff;
    --paper-tint: #f1f1f3;
  }
  * { box-sizing: border-box; margin: 0; padding: 0; }
  html, body { width: 1200px; height: 697px; overflow: hidden; }
  body {
    background: var(--bg);
    font-family: "Exo 2", Arial, sans-serif;
    position: relative;
  }
  .card {
    position: absolute;
    width: 520px;
    height: 297px;
    border-radius: 4px;
    overflow: hidden;
    box-shadow: 0 14px 30px rgba(0,0,0,0.45);
  }
  .card--front {
    left: 45px; top: 200px;
    background: linear-gradient(135deg, var(--purple-deep) 0%, var(--purple) 100%);
  }
  .card--back {
    left: 635px; top: 200px;
    background: var(--paper);
  }
  .brand { position: absolute; display: flex; align-items: center; }
  .brand__mark { display: block; }
  .brand__name { font-weight: 600; letter-spacing: 2px; text-transform: uppercase; line-height: 1; }
  .card--front .brand { left: 95px; top: 100px; }
  .card--front .brand__mark { width: 48px; height: 48px; background: var(--cyan); margin-right: 18px; }
  .card--front .brand__name { color: var(--paper); font-size: 52px; }
  .tagline {
    position: absolute; left: 162px; top: 160px;
    color: var(--paper); font-size: 15px; letter-spacing: 2px; font-weight: 500;
  }
  .card--back .brand { left: 32px; top: 30px; }
  .card--back .brand__mark { width: 22px; height: 22px; background: var(--cyan); margin-right: 10px; }
  .card--back .brand__name { color: var(--ink); font-size: 26px; }
  .watermark {
    position: absolute; right: -30px; top: 120px;
    font-size: 110px; font-weight: 600; color: var(--paper-tint);
    text-transform: uppercase; letter-spacing: 4px; line-height: 1;
  }
  .person { position: absolute; left: 32px; top: 84px; }
  .person__name { font-size: 19px; font-weight: 700; color: var(--ink); }
  .person__role { font-size: 12px; color: var(--cyan); margin-top: 2px; }
  .contact { position: absolute; left: 32px; top: 140px; list-style: none; font-size: 11px; color: var(--ink-soft); line-height: 1.6; }
  .contact__label { display: inline-block; width: 16px; }
  .address { position: absolute; left: 32px; top: 208px; font-size: 11.5px; color: var(--ink-soft); }
  .social { position: absolute; right: 24px; bottom: 22px; display: flex; gap: 8px; }
  .social__dot { width: 14px; height: 14px; border-radius: 50%; background: var(--cyan); }
</style>
</head>
<body>
  <section class="card card--front" aria-label="Card front">
    <div class="brand">
      <span class="brand__mark"></span>
      <span class="brand__name">Quorvex</span>
    </div>
    <p class="tagline">cloud communications</p>
  </section>

  <section class="card card--back" aria-label="Card back">
    <div class="watermark" aria-hidden="true">Quorvex</div>
    <div class="brand">
      <span class="brand__mark"></span>
      <span class="brand__name">Quorvex</span>
    </div>
    <div class="person">
      <h1 class="person__name">Marcus Ellwood</h1>
      <p class="person__role">Managing Director</p>
    </div>
    <ul class="contact">
      <li><span class="contact__label">t:</span>0917-555-0142</li>
      <li><span class="contact__label">e:</span>marcus@quorvexmail.com</li>
      <li><span class="contact__label">w:</span>www.quorvexcloud.com</li>
    </ul>
    <p class="address">480 Harbor Crest Ave, Bayford, FL 33990</p>
    <div class="social" aria-label="Social links">
      <span class="social__dot"></span>
      <span class="social__dot"></span>
      <span class="social__dot"></span>
    </div>
  </section>
</body>
</html>
```